Presentation Folder Cover For Plumbing Company

We need a presentation folder cover (FRONT AND BACK) for our plumbing business.

We specialise in plumbing, hot water, electrical and pipe relining.

This will be sent to clients and the contents pages will outline all of our company details and information.

The target market for this cover is Strata / Property Managers who look after unit buildings.

Target Market(s)

Strata & Property Managers. The higher end of the property market.

Industry/Entity Type

Plumbing

Font styles to use
Sans Serif

Colors
ec1f27
0355a3
ffffff
474747
c9c9c9

Requirements
Must have
• A4 Paper Size
• Inviting to clients to open the document and read on.
Nice to have
• Sleek, Professional and Stands Out.
Should not have
• Dark Background. Needs to be fresh and bright.

```html
<!DOCTYPE html>
<html lang="en">
<head>
<meta charset="utf-8">
<title>Crestfield Contracting – Presentation Folder</title>
<link href="https://fonts.googleapis.com/css2?family=Poppins:wght@600;700&display=swap" rel="stylesheet">
<style>
  :root {
    --page-bg: #e6e6f7;
    --paper: #eceefa;
    --paper-light: #f4f5fd;
    --band-top: #c3c9e8;
    --band-deep: #aeb5dc;
    --wave-edge: #d5d9f0;
    --brand-blue: #0355a3;
    --text-dark: #232323;
    --shadow: rgba(60, 70, 130, 0.28);
  }
  * { margin: 0; padding: 0; box-sizing: border-box; }
  html, body {
    width: 1200px; height: 960px; overflow: hidden;
    background: radial-gradient(ellipse at center, #eeeefb 0%, var(--page-bg) 70%, #d9d9ee 100%);
    font-family: "Poppins", Arial, sans-serif;
  }
  .folder-spread {
    position: absolute; left: 200px; top: 191px;
    width: 800px; height: 562px;
    box-shadow: 0 6px 18px var(--shadow);
  }
  .folder-art { position: absolute; inset: 0; display: block; }
  .wave-layer { filter: drop-shadow(0 3px 4px rgba(70, 80, 140, 0.35)); }
  .front-brand {
    position: absolute; left: 400px; width: 400px; top: 326px;
    text-align: center;
  }
  .brand-name {
    font-weight: 700; font-size: 27px; line-height: 1.1;
    color: var(--brand-blue); letter-spacing: 0.3px;
  }
  .brand-services {
    margin-top: 10px;
    font-weight: 600; font-size: 12.5px; color: var(--text-dark);
  }
</style>
</head>
<body>
  <section class="folder-spread" aria-label="Presentation folder, back and front covers">
    <svg class="folder-art" viewBox="0 0 800 562" width="800" height="562" aria-hidden="true">
      <defs>
        <linearGradient id="paperGrad" x1="0" x2="1" y1="0" y2="0">
          <stop offset="0" stop-color="#eef0fb"/>
          <stop offset="0.45" stop-color="#f6f7fe"/>
          <stop offset="0.5" stop-color="#e3e6f6"/>
          <stop offset="1" stop-color="#e6e8f7"/>
        </linearGradient>
        <linearGradient id="bandGrad" x1="0" x2="1" y1="0" y2="1">
          <stop offset="0" stop-color="#d2d7f0"/>
          <stop offset="0.5" stop-color="#c6cced"/>
          <stop offset="1" stop-color="#b7bee3"/>
        </linearGradient>
        <linearGradient id="foldShade" x1="0" x2="1">
          <stop offset="0" stop-color="#ffffff" stop-opacity="0"/>
          <stop offset="0.49" stop-color="#ffffff" stop-opacity="0.25"/>
          <stop offset="0.5" stop-color="#8a90c0" stop-opacity="0.12"/>
          <stop offset="1" stop-color="#8a90c0" stop-opacity="0.06"/>
        </linearGradient>
      </defs>

      <!-- top band -->
      <rect class="band-top" width="800" height="562" fill="url(#bandGrad)"/>

      <!-- main paper with upper and lower wave edges -->
      <g class="wave-layer">
        <path d="M0 112 C120 105 260 98 400 102 C560 106 700 80 800 45 L800 500
                 C700 540 600 545 480 520 C380 500 300 455 200 440 C120 430 60 440 0 455 Z"
              fill="url(#paperGrad)"/>
      </g>

      <!-- second upper wave -->
      <g class="wave-layer">
        <path d="M0 118 C120 110 230 120 330 160 C440 205 560 230 660 215 C730 205 780 190 800 180
                 L800 500 C700 540 600 545 480 520 C380 500 300 455 200 440 C120 430 60 440 0 455 Z"
              fill="url(#paperGrad)"/>
      </g>

      <!-- lower wave band -->
      <g class="wave-layer">
        <path d="M0 460 C80 430 170 425 260 440 C340 452 400 470 480 505 C560 540 680 545 800 505
                 L800 562 L0 562 Z" fill="#c0c6e6"/>
      </g>
      <g class="wave-layer">
        <path d="M0 490 C90 460 200 462 300 480 C400 500 470 540 560 550 C660 560 740 540 800 530
                 L800 562 L0 562 Z" fill="#b3bae0"/>
      </g>

      <!-- fold shading -->
      <rect width="800" height="562" fill="url(#foldShade)"/>
      <line x1="400" y1="0" x2="400" y2="562" stroke="#c5c9e6" stroke-width="1"/>
    </svg>

    <div class="front-brand">
      <div class="brand-name">Crestfield Contracting</div>
      <div class="brand-services">Plumbing • Electrical • Hot Water</div>
    </div>
  </section>
</body>
</html>
```